Business cards and logo for kitchen and bath remodeling company

We want an elegant card but that calls attention something unique and when people see it they remember us. A log that we can use for our own. We are a kitchen and bathroom remodeling company. We are 3 partners staring the company we are located in seattle washington usa. We try to give the best experience and luxury look in our projects and we are looking to show that in our cards. I added a sample of a card I really like. I like the black and gold look but gray blue or green in a metallic look would look nice. I'm open to any color.

Target Market(s)

Home owners.

Industry/Entity Type

Construction

Contact Information for Business Card

Larchmont and Vey builders

Colors

Designer to choose colors to be used in the design.

Requirements
Must have
• Make a Logo
• Logo to be unique
• Name of company larchmont and vey builders
Nice to have
• Have a good color scheme
• Front design to connect with back of card

```html
<!DOCTYPE html>
<html lang="en">
<head>
<meta charset="utf-8">
<title>Larchmont and Vey builders – Business Cards</title>
<link rel="stylesheet" href="https://fonts.googleapis.com/css2?family=Ubuntu:wght@400;500;700&display=swap">
<style>
  :root {
    --canvas: #e6e7e9;
    --blue: #21409a;
    --silver: #bdbebf;
    --charcoal: #3a3e49;
    --gold: #c3952f;
    --ivory: #eeeeee;
  }
  * { margin: 0; padding: 0; box-sizing: border-box; }
  html, body { width: 1200px; height: 1200px; overflow: hidden; background: var(--canvas); }
  .canvas { position: relative; width: 1200px; height: 1200px; font-family: "Ubuntu", sans-serif; }

  .card { position: absolute; width: 325px; height: 185px; overflow: hidden; }
  .set-blue .card { background: var(--blue); color: var(--silver); }
  .set-dark .card { background: var(--charcoal); color: var(--ivory); }

  .set-blue .front { left: 255px; top: 380px; }
  .set-blue .back  { left: 594px; top: 380px; }
  .set-dark .front { left: 264px; top: 669px; }
  .set-dark .back  { left: 611px; top: 669px; }

  /* plain square split across the fold, joining front and back */
  .split-square { position: absolute; }
  .set-blue .split-square { background: var(--silver); top: 43px; height: 80px; }
  .set-dark .split-square { background: var(--gold); top: 41px; height: 84px; }
  .set-blue .front .split-square { left: 291px; width: 34px; }
  .set-blue .back .split-square  { left: 0; width: 32px; }
  .set-dark .front .split-square { left: 293px; width: 32px; }
  .set-dark .back .split-square  { left: 0; width: 30px; }

  .wordmark { position: absolute; width: 193px; }
  .set-blue .wordmark { left: 60px; top: 75px; }
  .set-dark .wordmark { left: 63px; top: 74px; width: 181px; }
  .wordmark-name {
    display: block; font-weight: 700; font-size: 17.5px; line-height: 20px;
    text-transform: uppercase; white-space: nowrap;
  }
  .set-dark .wordmark-name { font-size: 16.5px; }
  .wordmark-tail {
    display: flex; justify-content: space-between;
    font-size: 12.5px; font-weight: 400; line-height: 15px; text-transform: uppercase;
  }

  .contact { position: absolute; }
  .set-blue .contact { left: 96px; top: 62px; }
  .set-dark .contact { left: 99px; top: 70px; }
  .contact-name { font-weight: 700; font-size: 13.5px; line-height: 17px; margin-bottom: 1px; }
  .contact-line { font-size: 10px; letter-spacing: 0.14em; line-height: 14.5px; padding-left: 5px; }
</style>
</head>
<body>
<div class="canvas">
  <section class="card-set set-blue">
    <div class="card front">
      <div class="wordmark">
        <span class="wordmark-name">Larchmont and Vey</span>
        <span class="wordmark-tail"><span>B</span><span>U</span><span>I</span><span>L</span><span>D</span><span>E</span><span>R</span><span>S</span></span>
      </div>
      <div class="split-square"></div>
    </div>
    <div class="card back">
      <div class="split-square"></div>
      <div class="contact">
        <p class="contact-name">Marisol Dunbar</p>
        <p class="contact-line">Cell:206.555.0147</p>
        <p class="contact-line">Email:</p>
        <p class="contact-line">Web:</p>
      </div>
    </div>
  </section>

  <section class="card-set set-dark">
    <div class="card front">
      <div class="wordmark">
        <span class="wordmark-name">Larchmont and Vey</span>
        <span class="wordmark-tail"><span>B</span><span>U</span><span>I</span><span>L</span><span>D</span><span>E</span><span>R</span><span>S</span></span>
      </div>
      <div class="split-square"></div>
    </div>
    <div class="card back">
      <div class="split-square"></div>
      <div class="contact">
        <p class="contact-name">Marisol Dunbar</p>
        <p class="contact-line">Cell:206.555.0147</p>
        <p class="contact-line">Email:</p>
        <p class="contact-line">Web:</p>
      </div>
    </div>
  </section>
</div>
</body>
</html>
```